Landscape Contractor in need of New Web Design

HELP.. Please Help!!!!. Our current website is old, outdated, ugly... and well nothing like us.... so we are looking for someone to help build a new website that fits our company direction. We are a landscape company with multiple locations in order to meet the needs of our clients and their projects throughout the midwest. When most people think of landscaping, they think of mowing grandmas yard, but that is NOT even remotely close to what we do. We are 100% a commercial landscape company meaning we complete landscape and irrigation services for large scale commercial projects. We are looking for a website to showcase our commercial talents and awesome team of people.
Updates

Address of current website is www.brookvaleyardworks.com

```html
<!DOCTYPE html>
<html lang="en">
<head>
<meta charset="utf-8">
<title>Brookvale — Commercial Landscape Contractor</title>
<link href="https://fonts.googleapis.com/css2?family=Red+Hat+Display:wght@400;500;700;800&family=Rubik:wght@400;500&display=swap" rel="stylesheet">
<style>
:root{
  --green-deep:#0c4a24;
  --green:#125f30;
  --green-mid:#2d7a3e;
  --lime:#a8d414;
  --lime-dark:#8fb80c;
  --ink:#1d2a20;
  --muted:#6b756d;
  --line:#e3e7e2;
  --white:#ffffff;
  --paper:#f6f8f4;
}
*{box-sizing:border-box;margin:0;padding:0}
html,body{width:1200px;height:2932px;overflow:hidden}
body{font-family:"Rubik",sans-serif;color:var(--ink);background:var(--white);position:relative}
h1,h2,h3,h4,.brand-name{font-family:"Red Hat Display",sans-serif}
.abs{position:absolute}
.btn{display:inline-block;background:var(--lime);color:var(--green-deep);font:700 11px "Red Hat Display",sans-serif;text-transform:uppercase;letter-spacing:.5px;padding:11px 22px;border-radius:2px}

/* hero */
.hero{left:0;top:0;width:1200px;height:490px;background:linear-gradient(100deg,#2f5a2a 0%,#4f7d3a 45%,#7fa35a 70%,#3f6a32 100%)}
.hero::after{content:"";position:absolute;inset:0;background:linear-gradient(90deg,rgba(8,40,18,.55),rgba(8,40,18,.1) 70%)}
.site-header{left:0;top:0;width:1200px;height:110px;z-index:3}
.brand{left:292px;top:40px;display:flex;align-items:center;gap:8px}
.brand-dot{width:40px;height:40px;border-radius:50%;background:var(--lime)}
.brand-name{font-weight:800;font-size:20px;color:var(--white)}
.nav{left:450px;top:60px;display:flex;gap:26px;font-size:12px;color:var(--white);white-space:nowrap}
.nav .active{color:var(--lime)}
.header-call{left:840px;top:50px;color:var(--white);font-size:11px;line-height:16px;white-space:nowrap}
.header-call b{font:700 12px "Red Hat Display",sans-serif;color:var(--lime)}
.hero-copy{left:292px;top:210px;width:460px;color:var(--white);z-index:2}
.hero-copy h1{font-size:46px;line-height:52px;font-weight:500}
.hero-copy p{font-size:12px;line-height:19px;margin:24px 0 28px;opacity:.9}

/* contact strip */
.callout{left:300px;top:472px;width:220px;height:136px;background:var(--green);color:var(--white);display:flex;align-items:center;justify-content:center;gap:12px;z-index:3}
.callout svg{width:30px;height:30px}
.callout b{display:block;font:700 15px "Red Hat Display",sans-serif}
.callout span{font-size:11px;opacity:.85}
.quick-form{left:520px;top:472px;width:380px;height:136px;background:var(--white);box-shadow:0 6px 24px rgba(0,0,0,.12);padding:26px 22px;z-index:3;display:grid;grid-template-columns:1fr 1fr 1fr;gap:14px 12px;align-content:start}
.field{border-bottom:1px solid var(--line);font-size:10px;color:var(--muted);padding:6px 0}
.quick-form .btn{padding:8px 10px;font-size:9px;text-align:center}
.quick-form .note{grid-column:1/4;font-size:9px;color:var(--muted)}

/* services */
.eyebrow{font:500 11px "Rubik",sans-serif;color:var(--green-mid)}
.intro{left:292px;top:810px;width:220px}
.intro h2{font-size:34px;line-height:40px;font-weight:800;margin:12px 0 22px;color:var(--ink)}
.intro p{font-size:11px;line-height:18px;color:var(--muted);margin-bottom:14px}
.badges{display:flex;gap:14px;margin:22px 0 26px}
.badge{display:flex;align-items:center;gap:6px;font-size:10px;color:var(--ink)}
.badge i{width:28px;height:28px;border-radius:50%;background:var(--green-mid);display:block;flex:none}
.service-grid{left:532px;top:668px;display:grid;grid-template-columns:160px 160px;column-gap:30px}
.service-grid .col2{margin-top:20px}
.card{width:160px;background:var(--white);box-shadow:0 4px 16px rgba(0,0,0,.08);margin-bottom:26px}
.card .ph{height:140px}
.card .body{padding:12px 12px 16px}
.card h3{font-size:13px;font-weight:700;margin-bottom:6px}
.card p{font-size:9px;line-height:14px;color:var(--muted);margin-bottom:8px}
.card a{font-size:9px;color:var(--green-mid);font-weight:500}

/* achievement */
.achieve{left:0;top:1480px;width:1200px;height:340px;background:linear-gradient(90deg,#1f4d25 0%,#3d6e32 50%,#6c9550 100%)}
.achieve::after{content:"";position:absolute;inset:0;background:linear-gradient(90deg,rgba(10,50,20,.5),rgba(10,50,20,0) 60%)}
.achieve-copy{left:296px;top:1552px;color:var(--white);z-index:2}
.achieve-copy h2{font-size:34px;font-weight:500}
.achieve-copy p{font-size:11px;opacity:.85;margin-top:8px;width:300px;line-height:17px}
.stats{left:296px;top:1652px;display:flex;gap:20px;z-index:2}
.stat{width:86px;height:96px;background:var(--white);text-align:center;padding-top:16px}
.stat svg{width:20px;height:20px}
.stat b{display:block;font:800 20px "Red Hat Display",sans-serif;color:var(--green);margin-top:4px}
.stat span{font-size:8px;color:var(--muted)}

/* about */
.about-photo{left:296px;top:1880px;width:304px;height:390px;background:linear-gradient(160deg,#6aa342,#3c7a2c 60%,#c9a74a)}
.about-copy{left:648px;top:1980px;width:300px}
.about-copy h2{font-size:26px;line-height:32px;font-weight:700;margin:8px 0 12px}
.about-copy p{font-size:10px;line-height:16px;color:var(--muted)}
.ticks{display:grid;grid-template-columns:1fr 1fr;gap:10px;margin:18px 0 26px;list-style:none;font-size:10px;color:var(--ink)}
.ticks li{display:flex;align-items:center;gap:6px}
.ticks svg{width:11px;height:11px}

/* cta */
.cta{left:0;top:2280px;width:1200px;height:260px;background:linear-gradient(90deg,#1c4a22,#2c5f2c 50%,#173e1c)}
.cta-copy{left:0;top:2356px;width:1200px;text-align:center;color:var(--white);z-index:2}
.cta-copy h2{font-size:26px;font-weight:700}
.cta-copy p{font-size:10px;line-height:16px;opacity:.85;margin:10px auto 18px;width:380px}

/* footer */
.footer{left:0;top:2540px;width:1200px;height:392px;background:var(--green-deep);color:var(--white)}
.f-brand{left:296px;top:2592px;display:flex;align-items:center;gap:8px}
.f-contact{top:2600px;font-size:10px;line-height:15px;display:flex;gap:8px;color:var(--white);white-space:nowrap}
.f-contact svg{width:18px;height:18px;flex:none}
.f-contact b{display:block;font:700 10px "Red Hat Display",sans-serif;color:var(--lime)}
.f-rule{left:296px;top:2710px;width:640px;height:1px;background:rgba(255,255,255,.15)}
.f-col{top:2734px;font-size:9px;line-height:16px;color:rgba(255,255,255,.75)}
.f-col h4{font-size:10px;color:var(--white);margin-bottom:8px;text-transform:uppercase;letter-spacing:.5px}
.f-sub{display:flex;margin-top:8px}
.f-sub span{width:100px;height:22px;background:var(--white);display:block}
.f-sub i{width:22px;height:22px;background:var(--lime);display:block}
.socials{left:296px;top:2838px;display:flex;gap:10px}
.socials i{width:8px;height:8px;border-radius:50%;background:var(--lime);display:block}
.copyright{left:296px;top:2880px;font-size:8px;color:rgba(255,255,255,.6)}
</style>
</head>
<body>

<div class="abs hero" role="img" aria-label="Photo of a smiling gardener in an orange cap working among green shrubs"></div>
<header class="abs site-header">
  <div class="abs brand"><span class="brand-dot"></span><span class="brand-name">Brookvale</span></div>
  <nav class="abs nav"><span class="active">Home</span><span>About Us</span><span>Services</span><span>Projects</span><span>Contact</span></nav>
  <div class="abs header-call"><b>Get Quote</b><br>(555) 014-2286<br>(555) 014-2290</div>
</header>
<div class="abs hero-copy">
  <h1>Expert Gardener &amp; Best Service.</h1>
  <p>Commercial landscape and irrigation for large projects across the Midwest, delivered by a crew that takes pride in every site.</p>
  <span class="btn">Get Started</span>
</div>

<div class="abs callout">
  <svg viewBox="0 0 24 24" fill="none" stroke="#a8d414" stroke-width="2"><path d="M5 3h4l2 5-3 2a12 12 0 0 0 6 6l2-3 5 2v4a2 2 0 0 1-2 2A18 18 0 0 1 3 5a2 2 0 0 1 2-2z"/></svg>
  <div><b>Call Us Now</b><span>(555) 014-2286</span></div>
</div>
<form class="abs quick-form">
  <div class="field">Name</div><div class="field">Email Address</div><div class="field">Phone</div>
  <div class="field">Service</div><div class="field">Date</div><span class="btn">Get a Quote</span>
  <div class="note">We respond to every request within one business day.</div>
</form>

<section class="abs intro">
  <div class="eyebrow">Who We Are</div>
  <h2>We are a full service lawn and landscape contractor.</h2>
  <p>We build and care for commercial grounds across the Midwest, from new installs to full irrigation systems on large sites.</p>
  <p>Our crews plan, plant and maintain each property with care, so clients can count on clean, healthy spaces all season.</p>
  <div class="badges">
    <div class="badge"><i></i>Eco Friendly<br>Work</div>
    <div class="badge"><i></i>Trusted<br>Crews</div>
  </div>
  <span class="btn">Learn More</span>
</section>

<div class="abs service-grid">
  <div>
    <article class="card"><div class="ph" role="img" aria-label="Photo of a worker trimming a hedge" style="background:linear-gradient(160deg,#4f8a35,#2a5a24)"></div><div class="body"><h3>Maintenance</h3><p>Regular care that keeps commercial grounds neat and green.</p><a>Read More</a></div></article>
    <article class="card"><div class="ph" role="img" aria-label="Photo of fresh turf rolled onto soil" style="background:linear-gradient(160deg,#7db04a,#8a6a3c)"></div><div class="body"><h3>Turf Management</h3><p>Healthy lawns through seeding, feeding and careful mowing.</p><a>Read More</a></div></article>
    <article class="card"><div class="ph" role="img" aria-label="Photo of an irrigation sprinkler watering plants" style="background:linear-gradient(160deg,#5e9a3a,#b9c06a)"></div><div class="body"><h3>Irrigation</h3><p>Efficient water systems designed for large sites.</p><a>Read More</a></div></article>
  </div>
  <div class="col2">
    <article class="card"><div class="ph" role="img" aria-label="Photo of a gardener applying treatment to shrubs" style="background:linear-gradient(160deg,#3e7a2e,#6a9a44)"></div><div class="body"><h3>Chemical Applications &amp; Fertilization</h3><p>Targeted treatments for strong plants and clean beds.</p><a>Read More</a></div></article>
    <article class="card"><div class="ph" role="img" aria-label="Photo of a stone patio with planted borders" style="background:linear-gradient(160deg,#8a5a3c,#5a7a3a)"></div><div class="body"><h3>Hardscaping</h3><p>Walkways, walls and patios built to last.</p><a>Read More</a></div></article>
    <article class="card"><div class="ph" role="img" aria-label="Photo of a landscaper planting flowers" style="background:linear-gradient(160deg,#3f8a3a,#c14a4a)"></div><div class="body"><h3>Landscaping</h3><p>Plantings and design that lift every property.</p><a>Read More</a></div></article>
  </div>
</div>

<section class="abs achieve" role="img" aria-label="Photo of a smiling landscaper in a cap in a leafy garden"></section>
<div class="abs achieve-copy">
  <h2>The Achivement</h2>
  <p>Years of steady growth and proud clients across many commercial sites.</p>
</div>
<div class="abs stats">
  <div class="stat"><svg viewBox="0 0 24 24" fill="none" stroke="#2d7a3e" stroke-width="2"><path d="M4 12l5 5L20 6"/></svg><b>50</b><span>Projects Done</span></div>
  <div class="stat"><svg viewBox="0 0 24 24" fill="none" stroke="#2d7a3e" stroke-width="2"><path d="M4 12l5 5L20 6"/></svg><b>100</b><span>Happy Clients</span></div>
  <div class="stat"><svg viewBox="0 0 24 24" fill="none" stroke="#2d7a3e" stroke-width="2"><path d="M4 12l5 5L20 6"/></svg><b>120</b><span>Team Members</span></div>
</div>

<div class="abs about-photo" role="img" aria-label="Photo of a gardener in orange mowing a lawn with a green mower"></div>
<section class="abs about-copy">
  <div class="eyebrow">Why Choose Us</div>
  <h2>15 year of Professional landscaping</h2>
  <p>Our team brings long practice and proper equipment to every commercial project we take on.</p>
  <ul class="ticks">
    <li><svg viewBox="0 0 24 24" fill="none" stroke="#2d7a3e" stroke-width="3"><path d="M4 12l5 5L20 6"/></svg>Maintenance</li>
    <li><svg viewBox="0 0 24 24" fill="none" stroke="#2d7a3e" stroke-width="3"><path d="M4 12l5 5L20 6"/></svg>Hardscaping</li>
    <li><svg viewBox="0 0 24 24" fill="none" stroke="#2d7a3e" stroke-width="3"><path d="M4 12l5 5L20 6"/></svg>Fertilization</li>
    <li><svg viewBox="0 0 24 24" fill="none" stroke="#2d7a3e" stroke-width="3"><path d="M4 12l5 5L20 6"/></svg>Landscaping</li>
    <li><svg viewBox="0 0 24 24" fill="none" stroke="#2d7a3e" stroke-width="3"><path d="M4 12l5 5L20 6"/></svg>Turf Care</li>
    <li><svg viewBox="0 0 24 24" fill="none" stroke="#2d7a3e" stroke-width="3"><path d="M4 12l5 5L20 6"/></svg>Irrigation</li>
  </ul>
  <span class="btn">Learn More</span>
</section>

<section class="abs cta" role="img" aria-label="Photo of a curved garden path through a green lawn"></section>
<div class="abs cta-copy">
  <h2>Let's Begin A New Project with Us</h2>
  <p>Tell us about your site and our team will plan the right landscape and irrigation work for it.</p>
  <span class="btn">Contact Us</span>
</div>

<footer class="abs footer"></footer>
<div class="abs f-brand"><span class="brand-dot"></span><span class="brand-name">Brookvale</span></div>
<div class="abs f-contact" style="left:520px;top:2596px"><svg viewBox="0 0 24 24" fill="none" stroke="#a8d414" stroke-width="2"><path d="M5 3h4l2 5-3 2a12 12 0 0 0 6 6l2-3 5 2v4a2 2 0 0 1-2 2A18 18 0 0 1 3 5a2 2 0 0 1 2-2z"/></svg><div><b>Phone</b>(555) 014-2286<br>(555) 014-2290</div></div>
<div class="abs f-contact" style="left:640px;top:2620px"><svg viewBox="0 0 24 24" fill="none" stroke="#a8d414" stroke-width="2"><rect x="3" y="5" width="18" height="14"/><path d="M3 6l9 7 9-7"/></svg><div><b>Mail</b>hello@brookvaleyardworks.com</div></div>
<div class="abs f-contact" style="left:840px;top:2588px"><svg viewBox="0 0 24 24" fill="none" stroke="#a8d414" stroke-width="2"><path d="M12 22s7-7 7-12a7 7 0 0 0-14 0c0 5 7 12 7 12z"/><circle cx="12" cy="10" r="2.5"/></svg><div><b>Location</b>418 Alder Road<br>Cedar Falls, IA</div></div>
<div class="abs f-contact" style="left:840px;top:2646px"><svg viewBox="0 0 24 24" fill="none" stroke="#a8d414" stroke-width="2"><path d="M12 22s7-7 7-12a7 7 0 0 0-14 0c0 5 7 12 7 12z"/><circle cx="12" cy="10" r="2.5"/></svg><div><b>Location</b>77 Prairie Lane<br>Marion, OH</div></div>
<div class="abs f-rule"></div>
<div class="abs f-col" style="left:296px;width:170px"><h4>About Us</h4>We care for commercial grounds across the Midwest with skilled crews and clear plans.<br>Large sites, done right.</div>
<div class="abs f-col" style="left:488px"><h4>Quick Links</h4>Home<br>About Us<br>Projects<br>Contact</div>
<div class="abs f-col" style="left:590px"><h4>Service Links</h4>Maintenance<br>Turf Management<br>Irrigation<br>Hardscaping</div>
<div class="abs f-col" style="left:708px"><h4>Subscribe</h4>Get seasonal tips and news.<div class="f-sub"><span></span><i></i></div></div>
<div class="abs socials"><i></i><i></i><i></i><i></i></div>
<div class="abs copyright">© 2024 Brookvale. All rights reserved. www.brookvaleyardworks.com</div>

</body>
</html>
```